Halvorsen Landscaping Truck Design

I want new design. I have posted our past designs but want new fresh clean and modern design. We are a high end landscape installation and. maintenance company that has had legacy in business for generations.

I have attached all logos (Halvorsen landscaping & Larkfield Vale trees) and the types of trucks we use. Q 240 , q 460, and tree trucks

Preferred both logos be used throughout

https://halvorsenlandscaping.com/landscape-services/landscape-construction-dallas/?gclid=Xm7PLtwRbUaZDhQNERIsBBDtcgLpwrU_dMh6lsb0zEgOkYp4gcDXZrvFMu5_-pPUx2MkrUyft9MbBq81FBMx_xcC

website for examples of work

Target Market(s)

high net worth residential accounts

Industry/Entity Type

landscaping / construction

Requirements
Must have
• clean/simple/luxury branding

```html
<!DOCTYPE html>
<html lang="en">
<head>
<meta charset="utf-8">
<title>Halvorsen Landscaping – Truck Wrap</title>
<link rel="stylesheet" href="https://fonts.googleapis.com/css2?family=Oswald:wght@500;700&family=Montserrat:wght@500&display=swap">
<style>
  :root {
    --wrap-black: #0d0d0d;
    --wrap-green: #0b7a2e;
    --wrap-green-dark: #07591f;
    --wrap-yellow: #f2c21b;
    --wrap-white: #ffffff;
    --page: #ffffff;
  }
  html, body {
    margin: 0;
    padding: 0;
    width: 1200px;
    height: 1200px;
    overflow: hidden;
    background: var(--page);
  }
  .canvas {
    position: relative;
    width: 1200px;
    height: 1200px;
  }
  .wrap-panel {
    position: absolute;
    left: 60px;
    top: 470px;
    width: 1080px;
    height: 260px;
  }
  .wrap-shapes {
    position: absolute;
    inset: 0;
    width: 100%;
    height: 100%;
  }
  .brand-name {
    position: absolute;
    left: 40px;
    top: 34px;
    width: 500px;
    margin: 0;
    text-align: center;
    font-family: "Oswald", sans-serif;
    font-weight: 700;
    color: var(--wrap-yellow);
    line-height: 1;
  }
  .brand-name .brand-main {
    display: block;
    font-size: 84px;
    line-height: 96px;
    letter-spacing: 2px;
  }
  .brand-name .brand-sub {
    display: block;
    font-size: 18px;
    line-height: 22px;
    letter-spacing: 3px;
    margin-top: 4px;
  }
  .phone {
    position: absolute;
    left: 18px;
    top: 191px;
    margin: 0;
    font-family: "Oswald", sans-serif;
    font-weight: 700;
    font-size: 26px;
    letter-spacing: 1px;
    color: var(--wrap-yellow);
    line-height: 30px;
  }
  .website {
    position: absolute;
    left: 260px;
    top: 199px;
    margin: 0;
    font-family: "Montserrat", sans-serif;
    font-weight: 500;
    font-size: 13px;
    color: var(--wrap-white);
    line-height: 16px;
  }
  .services {
    position: absolute;
    right: 22px;
    top: 34px;
    width: 380px;
    margin: 0;
    font-family: "Oswald", sans-serif;
    font-weight: 500;
    font-size: 15px;
    line-height: 1.25;
    color: var(--wrap-white);
    text-align: center;
    text-transform: uppercase;
  }
  .services .sep { color: var(--wrap-yellow); padding: 0 3px; }
  .tree-brand {
    position: absolute;
    right: 28px;
    top: 182px;
    display: flex;
    align-items: center;
    gap: 8px;
    font-family: "Oswald", sans-serif;
    font-weight: 700;
    font-size: 15px;
    color: var(--wrap-white);
    text-transform: uppercase;
    line-height: 1;
  }
  .tree-brand .mark {
    width: 14px;
    height: 14px;
    background: var(--wrap-green);
  }
</style>
</head>
<body>
<main class="canvas">
  <section class="wrap-panel" aria-label="Truck side wrap artwork">
    <svg class="wrap-shapes" viewBox="0 0 1080 260" preserveAspectRatio="none" aria-hidden="true">
      <rect class="base" x="0" y="0" width="1080" height="260" fill="var(--wrap-black)"/>
      <rect x="0" y="186" width="566" height="40" fill="var(--wrap-green)"/>
      <polygon points="566,226 566,186 684,20 1080,20 1080,150 800,150 722,226" fill="var(--wrap-green)"/>
      <polygon points="900,20 1080,20 1080,150 960,150" fill="var(--wrap-green-dark)" opacity="0.35"/>
      <polygon points="0,178 556,178 676,12 690,12 566,186 0,186" fill="var(--wrap-yellow)"/>
      <polygon points="704,12 712,12 588,186 580,186" fill="var(--wrap-yellow)"/>
      <polygon points="722,234 800,158 1080,158 1080,150 800,150 722,226 0,226 0,234" fill="var(--wrap-yellow)"/>
      <polygon points="744,244 818,170 1080,170 1080,165 815,165 738,244" fill="var(--wrap-yellow)"/>
    </svg>

    <h1 class="brand-name">
      <span class="brand-main">HALVORSEN</span>
      <span class="brand-sub">LANDSCAPING, INC.</span>
    </h1>

    <p class="phone">555★014★TREE</p>
    <p class="website">www.larkfieldvaletrees.com</p>

    <p class="services">
      Trimming<span class="sep">|</span>Removal<span class="sep">|</span>Fertilization<span class="sep">|</span>Stump Grinding<br>
      Cabling<span class="sep">|</span>Diagnosis<span class="sep">|</span>Spraying<span class="sep">|</span>Moving
    </p>

    <div class="tree-brand">
      <span class="mark"></span>
      <span>Larkfield Vale Trees</span>
    </div>
  </section>
</main>
</body>
</html>
```